Progressive Flow Chart

Looking for a progressive flow chart centered and branching off. They all build on each other 1-3. There will be 3 different pages.

Target Market(s)

Business Owners - High Net worth Individuals

Industry/Entity Type

Finance & Business Consulting

Font styles to use
Serif

Colors
0054AA
0677BA
7BADD7
CADEEF
E8F1F8
0094D4
00A9DD
6FCCEA
C7EBF8
E9F6FB
00AB8E
00BBA5
67D7C9
C6EFE9
E9F9F6

Requirements
Nice to have
• Clean, simple, and approachable.
Should not have
• Very Busy

```html
<!DOCTYPE html>
<html lang="en">
<head>
<meta charset="utf-8">
<title>Northvale Wealth – Living Trust Structure</title>
<link rel="stylesheet" href="https://fonts.googleapis.com/css2?family=Exo+2:wght@500;600;700&family=Ubuntu:wght@400;500&display=swap">
<style>
  :root{
    --page:#f6f6f6;
    --navy:#0d1845;
    --navy-deep:#0b133b;
    --navy-mid:#10285e;
    --blue:#2a9fe0;
    --green:#0af0b0;
    --teal-dot:#3fe0d0;
    --white:#ffffff;
    --brand:#3fb8e6;
  }
  html,body{margin:0;padding:0;width:1200px;height:998px;overflow:hidden;background:var(--page);}
  .chart{display:block;width:1200px;height:998px;}
  .heading{font-family:"Exo 2",sans-serif;font-weight:700;}
  .brand-name{font-family:"Exo 2",sans-serif;font-weight:600;font-size:21px;fill:var(--brand);letter-spacing:1px;}
  .node-title{font-family:"Exo 2",sans-serif;font-weight:700;font-size:19px;letter-spacing:.5px;}
  .node-note{font-family:"Ubuntu",sans-serif;font-size:11.5px;fill:var(--white);}
  .flow-label{font-family:"Ubuntu",sans-serif;font-weight:500;font-size:12.5px;fill:var(--white);}
  .ring-label{font-family:"Exo 2",sans-serif;font-weight:700;font-size:18px;fill:var(--white);}
  .step-num{font-family:"Exo 2",sans-serif;font-weight:700;fill:var(--navy-deep);}
  .badge-num{font-family:"Exo 2",sans-serif;font-weight:700;font-size:22px;fill:var(--green);}
  .badge-notch{fill:var(--navy-deep);}
  .flow{fill:none;stroke:var(--teal-dot);stroke-width:2;stroke-dasharray:0.1 4.5;stroke-linecap:round;}
  .box{fill:var(--navy-deep);stroke:url(#brandGrad);stroke-width:3.5;}
  .halo{fill:none;stroke:var(--white);stroke-width:1.2;}
  .icon-line{fill:none;stroke:var(--navy-deep);stroke-width:3;stroke-linejoin:round;stroke-linecap:round;}
  .icon-fill{fill:var(--navy-deep);}
</style>
</head>
<body>
<svg class="chart" viewBox="0 0 1200 998" xmlns="http://www.w3.org/2000/svg">
  <defs>
    <linearGradient id="brandGrad" x1="0" y1="0" x2="1" y2="0">
      <stop offset="0" stop-color="#2a9fe0"/>
      <stop offset="1" stop-color="#0af0b0"/>
    </linearGradient>
    <linearGradient id="brandGradDiag" x1="0" y1="1" x2="1" y2="0">
      <stop offset="0" stop-color="#2a9fe0"/>
      <stop offset="1" stop-color="#0af0b0"/>
    </linearGradient>
    <linearGradient id="panelGrad" x1="0" y1="0" x2="1" y2="1">
      <stop offset="0" stop-color="#0f2a66"/>
      <stop offset=".55" stop-color="#0d1c4f"/>
      <stop offset="1" stop-color="#0c143d"/>
    </linearGradient>
    <marker id="head" viewBox="0 0 10 10" refX="5" refY="5" markerWidth="9" markerHeight="9" orient="auto-start-reverse" markerUnits="userSpaceOnUse">
      <path d="M0,0 L10,5 L0,10 L3,5 Z" fill="#3fe0d0"/>
    </marker>
    <path id="trustArc" d="M527,452 A100,100 0 0 1 709,452"/>
  </defs>

  <!-- panel -->
  <rect class="panel" x="80" y="88" width="1045" height="807" fill="url(#panelGrad)"/>
  <rect class="panel-texture" x="80" y="88" width="1045" height="530" fill="#1a4590" opacity=".18" role="img" aria-label="Faint network of connected dots across the upper background"/>

  <!-- brand -->
  <g class="brand">
    <circle cx="248" cy="232" r="20" fill="none" stroke="var(--brand)" stroke-width="5"/>
    <text class="brand-name" x="248" y="300" text-anchor="middle">NORTHVALE WEALTH</text>
  </g>

  <!-- tier 3 connector -->
  <line class="flow" x1="530" y1="263" x2="663" y2="263"/>
  <line class="flow" x1="777" y1="263" x2="889" y2="263"/>

  <!-- tier 3 vehicles -->
  <g class="vehicle" transform="translate(472,264)">
    <circle class="halo" r="56"/>
    <circle r="51" fill="var(--navy-deep)" stroke="url(#brandGradDiag)" stroke-width="6"/>
    <rect x="-44" y="33" width="88" height="40" fill="var(--navy-deep)"/>
    <text class="ring-label" y="-2" text-anchor="middle" dominant-baseline="middle">CRT</text>
    <path d="M0,25 L24,70 Q0,58 -24,70 Z" fill="url(#brandGradDiag)"/>
    <text class="step-num" x="0" y="59" font-size="20" text-anchor="middle">3</text>
  </g>
  <g class="vehicle" transform="translate(719,266)">
    <circle class="halo" r="56"/>
    <circle r="51" fill="var(--navy-deep)" stroke="url(#brandGradDiag)" stroke-width="6"/>
    <rect x="-44" y="33" width="88" height="40" fill="var(--navy-deep)"/>
    <text class="ring-label" y="0" text-anchor="middle" dominant-baseline="middle">DAF</text>
    <path d="M0,25 L24,70 Q0,58 -24,70 Z" fill="url(#brandGradDiag)"/>
    <text class="step-num" x="0" y="59" font-size="20" text-anchor="middle">3</text>
  </g>
  <g class="vehicle" transform="translate(945,268)">
    <circle class="halo" r="56"/>
    <circle r="51" fill="var(--navy-deep)" stroke="url(#brandGradDiag)" stroke-width="6"/>
    <rect x="-44" y="33" width="88" height="40" fill="var(--navy-deep)"/>
    <text class="ring-label" y="-7" text-anchor="middle">GRAT’S</text>
    <text class="ring-label" y="13" text-anchor="middle">ID GT</text>
    <path d="M0,25 L24,70 Q0,58 -24,70 Z" fill="url(#brandGradDiag)"/>
    <text class="step-num" x="0" y="59" font-size="20" text-anchor="middle">3</text>
  </g>

  <!-- flows -->
  <g class="flows">
    <line class="flow" x1="483" y1="511" x2="354" y2="511" marker-end="url(#head)"/>
    <text class="flow-label" x="423" y="531" text-anchor="middle">INVEST</text>

    <line class="flow" x1="174" y1="727" x2="174" y2="574" marker-end="url(#head)"/>
    <text class="flow-label" transform="translate(163,648) rotate(-90)" text-anchor="middle">INTEREST</text>

    <line class="flow" x1="300" y1="573" x2="300" y2="648" marker-end="url(#head)"/>
    <line class="flow" x1="300" y1="648" x2="300" y2="720"/>
    <text class="flow-label" transform="translate(322,648) rotate(-90)" text-anchor="middle">INVESTMENT</text>

    <line class="flow" x1="339" y1="573" x2="504" y2="684" marker-end="url(#head)"/>
    <line class="flow" x1="504" y1="684" x2="561" y2="724"/>

    <line class="flow" x1="372" y1="687" x2="300" y2="724" marker-end="url(#head)"/>
    <line class="flow" x1="372" y1="687" x2="531" y2="594" marker-end="url(#head)"/>
    <text class="flow-label" transform="translate(392,704) rotate(-28)" text-anchor="middle">INCOME</text>

    <line class="flow" x1="519" y1="792" x2="357" y2="792" marker-end="url(#head)"/>
    <text class="flow-label" x="436" y="782" text-anchor="middle">RENT</text>

    <line class="flow" x1="620" y1="663" x2="620" y2="632" marker-end="url(#head)"/>
    <text class="flow-label" x="645" y="653">INCOME</text>

    <line class="flow" x1="732" y1="564" x2="918" y2="690"/>
    <line class="flow" x1="711" y1="591" x2="906" y2="726"/>
  </g>

  <!-- tier 1 centre -->
  <g class="living-trust">
    <circle cx="618" cy="492" r="128" fill="var(--navy-deep)" stroke="url(#brandGradDiag)" stroke-width="13"/>
    <text class="heading" font-size="25" fill="var(--white)" letter-spacing="2">
      <textPath href="#trustArc" startOffset="50%" text-anchor="middle">LIVING TRUST</textPath>
    </text>
    <circle cx="618" cy="496" r="74" fill="url(#brandGradDiag)"/>
    <text class="heading" x="616" y="494" font-size="24" fill="var(--navy-deep)" text-anchor="middle">YOU</text>
    <text class="heading" x="616" y="518" font-size="24" fill="var(--navy-deep)" text-anchor="middle">TRUSTEE</text>
    <path d="M726,452 Q722,446 732,449 L814,486 Q822,492 814,498 L732,536 Q722,540 726,532 Q740,492 726,452 Z" fill="url(#brandGrad)"/>
    <text class="step-num" x="766" y="510" font-size="44" text-anchor="middle">1</text>
  </g>

  <!-- bank -->
  <g class="node node-bank">
    <rect class="box" x="135" y="459" width="213" height="108" rx="12"/>
    <path class="halo" d="M189,440 A50,50 0 0 1 287,440"/>
    <circle cx="238" cy="453" r="42" fill="url(#brandGradDiag)"/>
    <circle class="badge-notch" cx="236" cy="405" r="15"/>
    <text class="badge-num" x="236" y="413" text-anchor="middle">2</text>
    <g class="icon">
      <path class="icon-fill" d="M238,430 L262,443 L214,443 Z"/>
      <rect class="icon-fill" x="216" y="445" width="44" height="4"/>
      <rect class="icon-fill" x="220" y="451" width="5" height="14"/>
      <rect class="icon-fill" x="230" y="451" width="5" height="14"/>
      <rect class="icon-fill" x="241" y="451" width="5" height="14"/>
      <rect class="icon-fill" x="251" y="451" width="5" height="14"/>
      <rect class="icon-fill" x="214" y="467" width="48" height="5"/>
    </g>
    <text class="node-title" x="237" y="521" text-anchor="middle" fill="url(#brandGrad)">BANK</text>
    <text class="node-note" x="238" y="539" text-anchor="middle">Makes Investments To</text>
    <text class="node-note" x="238" y="554" text-anchor="middle">Real estate + Business</text>
  </g>

  <!-- real estate -->
  <g class="node node-real-estate">
    <rect class="box" x="135" y="731" width="213" height="106" rx="12"/>
    <path class="halo" d="M189,712 A50,50 0 0 1 287,712"/>
    <circle cx="238" cy="725" r="42" fill="url(#brandGradDiag)"/>
    <circle class="badge-notch" cx="236" cy="677" r="15"/>
    <text class="badge-num" x="236" y="685" text-anchor="middle">1</text>
    <g class="icon">
      <path class="icon-line" d="M216,728 L238,708 L260,728"/>
      <path class="icon-line" d="M222,723 L222,744 L254,744 L254,723"/>
      <rect class="icon-fill" x="233" y="731" width="10" height="13"/>
    </g>
    <text class="node-title" x="239" y="790" text-anchor="middle" fill="url(#brandGrad)">REAL ESTATE</text>
    <text class="node-note" x="233" y="809" text-anchor="middle">LLC</text>
  </g>

  <!-- business -->
  <g class="node node-business">
    <rect class="box" x="522" y="729" width="213" height="108" rx="12"/>
    <path class="halo" d="M576,712 A50,50 0 0 1 672,712"/>
    <circle cx="624" cy="723" r="42" fill="url(#brandGradDiag)"/>
    <circle class="badge-notch" cx="624" cy="684" r="15"/>
    <text class="badge-num" x="624" y="692" text-anchor="middle">1</text>
    <g class="icon">
      <rect class="icon-fill" x="603" y="734" width="7" height="13"/>
      <rect class="icon-fill" x="613" y="728" width="7" height="19"/>
      <rect class="icon-fill" x="623" y="722" width="7" height="25"/>
      <rect class="icon-fill" x="633" y="716" width="7" height="31"/>
      <path class="icon-line" d="M604,727 L614,719 L625,714 L639,704" stroke-width="2.2"/>
      <circle class="icon-fill" cx="639" cy="704" r="3"/>
    </g>
    <text class="node-title" x="627" y="792" text-anchor="middle" fill="url(#brandGrad)">BUSINESS</text>
    <text class="node-note" x="553" y="810">LLC - MEMBER/MANAGER</text>
    <text class="node-note" x="553" y="825">CORP = PRESIDENT</text>
  </g>

  <!-- insurance -->
  <g class="node node-insurance">
    <rect class="box" x="852" y="731" width="213" height="106" rx="12"/>
    <path class="halo" d="M906,714 A50,50 0 0 1 1004,714"/>
    <circle cx="955" cy="725" r="42" fill="url(#brandGradDiag)"/>
    <circle class="badge-notch" cx="951" cy="680" r="15"/>
    <text class="badge-num" x="951" y="688" text-anchor="middle">2</text>
    <g class="icon">
      <path class="icon-line" d="M955,705 L970,711 L970,726 Q970,739 955,746 Q940,739 940,726 L940,711 Z"/>
      <path class="icon-line" d="M948,726 L953,731 L963,720" stroke-width="2.6"/>
    </g>
    <text class="node-title" x="960" y="793" text-anchor="middle" fill="url(#brandGrad)">INSURANCE</text>
  </g>
</svg>
</body>
</html>
```